QuorraLink Business Card

We require a stunning business card for QuorraLink - a new digital marketing agency. The logo provided was designed by a graphic designer here on ArtHivePro.

www.quorralink-example.net - "Get more sales online"

What we do:
The business delivers website optimisation (Web design, social media strategy, digital strategies, SEO, PPC, conversion optimisation, email marketing) to get businesses more sales online.

The card must match the brand style which can be found on this website template:

http://layoutbazaar.example/item/plumline-adaptive-allpurpose-skin/full_screen_preview/7193046

It must have 'wow' factor so that you'll never forget QuorraLink - We're open to any materials, textures you think will work.

We don't want a boring run of the mill design - I can knock that up in Photoshop myself or use a template solution. It should be timeless and only need replacing should the contact details change.

The design should be eye catching, future proof, exceptionally chic, classy and oozing authority and confidence. QuorraLink services must not look cheap.

Here's some brilliant designs to point you in the right direction:

http://tidycraftz.example/30-superb-calling-cards/

The spec is for double sided, but we're open to your ideas. If it's going on an opaque or see through card, then of course a single side is preferable. Using creativity and thought on the medium for the card - shape - texture is desirable.

The strapline for the business is "Get more business online" please submit with / without strapline.
Updates

Please only submit your best 1-3 designs initially.

Target Market(s)

Business 2 Business - Local SMEs
Local professionals - Doctors, Dentists, Financials, Bespoke Retailers, Property companies - anyone with a decent budget to spend on digital marketing services and a high margin product or service to sell.

Industry/Entity Type

Graphic Designer

Requirements
Must have
• Text:
• name: Tom Walcroft
• position Digital Marketing Director
• mobile 07911 204 658
• website www.quorralink-example.net
Nice to have
• Check See http://tidycraftz.example/30-superb-calling-cards/ for ideas.
• LinkedIn and Twitter usernames if there is space and it works on the design.

```html
<!DOCTYPE html>
<html lang="en">
<head>
<meta charset="utf-8">
<title>QuorraLink Business Card</title>
<link rel="stylesheet" href="https://fonts.googleapis.com/css2?family=Open+Sans:wght@400;600;700&display=swap">
<style>
  :root {
    --backdrop: #3b3b3b;
    --card: #121212;
    --accent-red: #e8412c;
    --accent-teal: #1f5266;
    --text-light: #d8d8d8;
    --text-muted: #bdbdbd;
  }
  * { margin: 0; padding: 0; box-sizing: border-box; }
  html, body {
    width: 1200px;
    height: 819px;
    overflow: hidden;
  }
  body {
    background: var(--backdrop);
    font-family: "Open Sans", sans-serif;
    display: flex;
    align-items: center;
    justify-content: center;
    gap: 60px;
  }
  .card {
    position: relative;
    width: 525px;
    height: 300px;
    background: var(--card);
    border-radius: 3px;
    box-shadow: 0 14px 30px rgba(0,0,0,0.45);
    overflow: hidden;
  }

  /* Shared wordmark */
  .wordmark {
    display: flex;
    align-items: center;
    gap: 10px;
  }
  .wordmark__dot {
    width: 22px;
    height: 22px;
    border-radius: 50%;
    background: var(--accent-red);
    flex: none;
  }
  .wordmark__name {
    font-weight: 700;
    font-size: 40px;
    line-height: 1;
    color: var(--accent-red);
    letter-spacing: -0.5px;
  }
  .tagline {
    margin-top: 6px;
    font-size: 10.5px;
    font-weight: 600;
    color: var(--text-light);
    letter-spacing: 0.1px;
  }

  /* Front */
  .card--front .brand {
    position: absolute;
    left: 190px;
    top: 118px;
  }

  /* Back */
  .card--back .brand {
    position: absolute;
    left: 34px;
    top: 34px;
  }
  .person {
    position: absolute;
    left: 34px;
    top: 128px;
  }
  .person__name {
    font-size: 14px;
    font-weight: 600;
    color: var(--accent-red);
  }
  .person__name span { color: var(--accent-teal); }
  .person__role {
    font-size: 11px;
    color: var(--text-light);
  }
  .contacts {
    position: absolute;
    left: 34px;
    top: 178px;
    list-style: none;
  }
  .contacts li {
    display: flex;
    align-items: center;
    gap: 8px;
    font-size: 11px;
    line-height: 17px;
    color: var(--text-light);
  }
  .contacts svg {
    width: 10px;
    height: 10px;
    fill: var(--accent-red);
    flex: none;
  }
  .address {
    position: absolute;
    right: 30px;
    bottom: 30px;
    font-size: 11px;
    line-height: 15px;
    color: var(--text-muted);
  }
</style>
</head>
<body>

  <section class="card card--front" aria-label="Card front">
    <div class="brand">
      <div class="wordmark">
        <span class="wordmark__dot"></span>
        <span class="wordmark__name">QuorraLink</span>
      </div>
      <p class="tagline">Visibility on the internet for business websites</p>
    </div>
  </section>

  <section class="card card--back" aria-label="Card back">
    <div class="brand">
      <div class="wordmark">
        <span class="wordmark__dot"></span>
        <span class="wordmark__name">QuorraLink</span>
      </div>
      <p class="tagline">Visibility on the internet for business websites</p>
    </div>

    <div class="person">
      <p class="person__name">Employee <span>name</span></p>
      <p class="person__role">CEO</p>
    </div>

    <ul class="contacts">
      <li>
        <svg viewBox="0 0 10 10" aria-hidden="true"><path d="M2 0.5 L3.6 2.8 L2.8 3.8 Q4 6 6.2 7.2 L7.2 6.4 L9.5 8 L8.3 9.5 Q1 8 0.5 1.7 Z"/></svg>
        555-555-5555
      </li>
      <li>
        <svg viewBox="0 0 10 10" aria-hidden="true"><rect x="2.5" y="0.5" width="5" height="9" rx="1"/><rect x="3.5" y="1.6" width="3" height="5" fill="#121212"/></svg>
        555-555-5555
      </li>
      <li>
        <svg viewBox="0 0 10 10" aria-hidden="true"><rect x="0.5" y="2" width="9" height="6.5" rx="0.8"/><path d="M1 2.6 L5 5.6 L9 2.6" stroke="#121212" stroke-width="0.9" fill="none"/></svg>
        info@quorralink-example.net
      </li>
      <li>
        <svg viewBox="0 0 10 10" aria-hidden="true"><circle cx="5" cy="5" r="4.5"/><path d="M0.8 5 H9.2 M5 0.6 Q2.4 5 5 9.4 M5 0.6 Q7.6 5 5 9.4" stroke="#121212" stroke-width="0.8" fill="none"/></svg>
        www.quorralink-example.net
      </li>
    </ul>

    <p class="address">Street name, city name,<br>zip code with country</p>
  </section>

</body>
</html>
```